Kestrel Wiring - Electrician company flyers for new clients

I want a flyer that will be dropped into mailboxes and will hopefully stand out more that the ones i have tried to mock up. I have attached my latest design to give you an idea but it is rather boring.

The aim is obviously to entice new customers into calling me for any electrical work, mainly domestic but i also do commercial work.
I will also upload a photo of my business card so that it can be used as a reference and my website is www.kestrelwiring.co.nz for any extra information.

Ideally the flyer will be DL size
measurements from printmorrow is that's any help
Document Trim Size
99 x 210 mm
1169 x 2480 pixels
Full Bleed Size
102 x 213 mm
1205 x 2516 pixels

Target Market(s)

Domestic electrical works

Industry/Entity Type

Electrician

Requirements
Must have
• all of my contact details -
• Dean Forsyth
• Dean@kestrelwiring.co.nz
• 027 3815 942
• www.kestrelwiring.co.nz
• A little write up similar to the one written on my draft but there's probably alot of room for improvement as my writing skills are lacking.
Nice to have
• clear and concise writing so that people wont throw it away before reading

```html
<!DOCTYPE html>
<html lang="en">
<head>
<meta charset="utf-8">
<title>Kestrel Wiring – DL Flyer</title>
<link rel="stylesheet" href="https://fonts.googleapis.com/css2?family=Raleway:ital,wght@0,300;0,400;0,500;0,600;0,700;1,500;1,600;1,800&display=swap">
<style>
  :root{
    --blue:#1f9fdb;
    --grey:#7b7d80;
    --grey-dark:#6a6c6f;
    --ink:#2c2c2c;
    --paper:#ffffff;
    --backdrop:#d9d9db;
    --photo-dark:#3d3430;
    --photo-mid:#6e6658;
    --photo-warm:#c7b58a;
  }
  *{box-sizing:border-box;margin:0;padding:0}
  html,body{width:1200px;height:1004px;overflow:hidden}
  body{background:var(--backdrop);font-family:"Raleway",sans-serif;color:var(--ink);position:relative}

  .flyer{position:absolute;left:380px;top:36px;width:440px;height:932px;background:var(--paper);overflow:hidden;box-shadow:0 6px 22px rgba(0,0,0,.18)}

  /* header */
  .flyer-header{height:97px;position:relative}
  .brand{position:absolute;left:20px;top:30px;display:flex;align-items:center;gap:8px}
  .brand-dot{width:14px;height:14px;border-radius:50%;background:var(--blue)}
  .brand-name{font-weight:700;font-size:22px;color:var(--grey-dark);letter-spacing:.5px}
  .tagline{position:absolute;right:13px;top:18px;text-align:right;font-style:italic;line-height:1}
  .tagline-main{display:block;font-weight:600;font-size:32px;color:var(--blue)}
  .tagline-sub{display:block;font-weight:500;font-size:24px;color:var(--grey);margin-top:2px}

  /* hero */
  .hero{position:relative;height:249px}
  .hero svg{position:absolute;left:0;top:0}
  .hero-headline{position:absolute;right:13px;top:20px;text-align:right;color:#fff;font-style:italic;font-weight:800;font-size:30px;line-height:36px;text-transform:uppercase}

  /* body copy */
  .services-bg{position:absolute;left:0;top:420px;width:440px;height:390px;background:radial-gradient(ellipse at 40% 50%,rgba(200,205,212,.22),rgba(255,255,255,0) 70%)}
  .services{position:absolute;left:15px;right:16px;top:360px}
  .service{margin-bottom:17px}
  .service-title{font-weight:500;font-size:21px;color:var(--grey-dark);line-height:26px;margin-bottom:5px}
  .service-title span{color:var(--blue)}
  .service-text{font-weight:300;font-size:17.4px;line-height:21.5px;text-align:justify;letter-spacing:-.45px}

  /* footer */
  .footer{position:absolute;left:0;bottom:0;width:440px;height:117px}
  .footer svg{position:absolute;left:0;top:0}
  .call-line{position:absolute;left:15px;top:1px;font-style:italic;font-weight:500;font-size:15.5px;color:#fff;white-space:nowrap}
  .contact-list{position:absolute;left:15px;top:35px;list-style:none}
  .contact-list li{display:flex;align-items:center;gap:7px;font-size:12.5px;color:var(--grey);height:17.5px;white-space:nowrap}
  .contact-list svg{position:static;flex:none}
  .contact-cta{position:absolute;left:240px;right:0;top:49px;text-align:center;font-weight:300;font-size:22px;color:#fff;letter-spacing:.3px;white-space:nowrap}
</style>
</head>
<body>
  <main class="flyer">
    <header class="flyer-header">
      <div class="brand"><span class="brand-dot"></span><span class="brand-name">Kestrel Wiring</span></div>
      <p class="tagline"><span class="tagline-main">Reliable and</span><span class="tagline-sub">Professional</span></p>
    </header>

    <section class="hero">
      <svg width="440" height="249" viewBox="0 0 440 249">
        <defs>
          <radialGradient id="lampGlow" cx="32%" cy="55%" r="60%">
            <stop offset="0" stop-color="var(--photo-warm)"/>
            <stop offset=".45" stop-color="var(--photo-mid)"/>
            <stop offset="1" stop-color="var(--photo-dark)"/>
          </radialGradient>
        </defs>
        <rect role="img" aria-label="Photo of an industrial caged pendant light glowing warm" x="0" y="0" width="440" height="227" fill="url(#lampGlow)"/>
        <polygon points="298,0 440,0 440,227 220,227" fill="var(--blue)"/>
        <polygon points="0,227 223,227 216,249 0,249" fill="var(--blue)"/>
        <polygon points="229,227 440,227 440,249 222,249" fill="var(--grey)"/>
      </svg>
      <h1 class="hero-headline">Do you<br>need a<br>local and<br>reliable<br>elecrician?</h1>
    </section>

    <div class="services-bg" role="img" aria-label="Faint electrical floor plan behind the text"></div>
    <section class="services">
      <article class="service">
        <h2 class="service-title"><span>Reliable</span> Electricians</h2>
        <p class="service-text">Specializing in residential and commercial electrical services, we are dedicated to providing customer service that is second to none. Whether you need a small wiring fix or the full installation, we can get the job done right.</p>
      </article>
      <article class="service">
        <h2 class="service-title"><span>Flexible</span> Services</h2>
        <p class="service-text">We provide you with a full consultation to explain your available options so that you can choose the scope of work that’s right for your home or business and your budget.</p>
      </article>
      <article class="service">
        <h2 class="service-title"><span>Customer Satisfaction</span> Guaranteed</h2>
        <p class="service-text">We strive to save you both time and money by combining our deep experience, the highest quality parts and equipment, and our dedication to delivering exceptional service. We will not leave the job until you are satisfied.</p>
      </article>
    </section>

    <footer class="footer">
      <svg width="440" height="117" viewBox="0 0 440 117">
        <polygon points="0,0 218,0 211,22 0,22" fill="var(--grey)"/>
        <polygon points="228,0 440,0 440,117 187,117" fill="var(--blue)"/>
      </svg>
      <p class="call-line">Give us a call anytime</p>
      <ul class="contact-list">
        <li><svg width="12" height="12" viewBox="0 0 12 12"><circle cx="6" cy="6" r="6" fill="var(--blue)"/><circle cx="6" cy="4.5" r="2" fill="#fff"/><path d="M2.8 9.5a3.2 3 0 0 1 6.4 0z" fill="#fff"/></svg>Dean Forsyth</li>
        <li><svg width="12" height="12" viewBox="0 0 12 12"><circle cx="6" cy="6" r="6" fill="var(--blue)"/><path d="M3.6 3.2l1.3-.4.8 1.6-.8.6a4 4 0 0 0 2 2l.6-.8 1.6.8-.4 1.3C6 8.6 3.4 6 3.6 3.2z" fill="#fff"/></svg>027 3815 942</li>
        <li><svg width="12" height="12" viewBox="0 0 12 12"><circle cx="6" cy="6" r="6" fill="var(--blue)"/><rect x="3" y="4" width="6" height="4.2" fill="#fff"/><path d="M3 4l3 2.3L9 4" fill="none" stroke="var(--blue)" stroke-width=".7"/></svg>Dean@kestrelwiring.co.nz</li>
        <li><svg width="12" height="12" viewBox="0 0 12 12"><circle cx="6" cy="6" r="6" fill="var(--blue)"/><circle cx="6" cy="6" r="3.3" fill="none" stroke="#fff" stroke-width=".8"/><path d="M2.7 6h6.6M6 2.7v6.6" stroke="#fff" stroke-width=".7"/></svg>www.kestrelwiring.co.nz</li>
      </ul>
      <p class="contact-cta">CONTACT US</p>
    </footer>
  </main>
</body>
</html>
```